Brightfern World Learning is to provide global summer programs in the United States through which students from the US and China share experiences, intensive learning, and each other’s cultures. The program seeks to more fully prepare both the US and Chinese students for their college education and future careers in this interdependent world. Chinese students are individually paired with US Students where they will reside US students' home for the period of the program.

Current website: Brightfern World Learning

Need to support both English and Chinese with different font.

Project Deadline Extended
Reason: Because of Thanksgiving Holidays.

Dear Designers,

In order to generate the best design, I uploaded some photos from our global summer program. Please check:

http://brightfernworldlearning.org/photos/

Colette

My company Logo just added to the project.

Sorry for the late update.

Project Deadline Extended
Reason: Due to Thanksgiving holiday, I don't have enough time to provide feedback to all the designers. Colette

Project Deadline Extended
Reason: Holiday season. Need more time for designer and myself.

Target Market(s)

Grade K to 12 students and their parents to sign up the global summer program. Majority audience are from China.

Industry/Entity Type

College

Font styles to use
Sans Serif

Colors
3277b5

Requirements
Must have
• You may check my current website for the summer program content
www.brightfernworldlearning.org
Check these two clips to see what service we provided.
http://www.vidhaven.example/watch?v=7kR3nq41xTm&feature=vh.be
https://www.vidhaven.example/watch?v=W8d2JP6h4oZ

Company Logo are included in the attachment.

Some photos from summer program: http://brightfernworldlearning.org/photos/
The website should show the students one to one relationship.
The website should show homestay part.

I want Photo Slider on each page to share the fun activities.

Each program will be provide a video clip as a summery.

The website should support font of both English and Chinese. I like to see both Chinese and English on the same page instead of switch back and forth. I can add Chinese part later if you leave the room.

Nice to have
• I have a lot of paired pictures. I am wondering if I can use collage of photos as the background.

The design should be playful and fun!

```html
<!DOCTYPE html>
<html lang="en">
<head>
<meta charset="utf-8">
<title>Brightfern World Learning</title>
<link href="https://fonts.googleapis.com/css2?family=Roboto+Condensed:wght@400;700&family=Lato:wght@400;700&family=Noto+Serif+SC:wght@400&display=swap" rel="stylesheet">
<style>
:root{
  --blue:#3277b5;
  --blue-deep:#1f68ad;
  --footer-blue:#1d6db4;
  --red:#b3122b;
  --ink:#4a4a4a;
  --dark:#2b2b2b;
  --page:#f1f2f4;
  --cn-blue:#2a8ee0;
}
*{box-sizing:border-box;margin:0;padding:0}
html,body{width:946px;height:1200px;overflow:hidden}
body{position:relative;background:var(--page);font-family:"Lato",sans-serif;color:var(--ink)}
.abs{position:absolute}
.masthead{left:0;top:0;width:946px;height:368px;background:linear-gradient(180deg,#3a3a3a,#2a2a2a 60%,#353535)}
.masthead-collage{left:0;top:0;width:946px;height:368px;background:repeating-linear-gradient(90deg,rgba(255,255,255,.03) 0 60px,rgba(0,0,0,.05) 60px 120px)}
.top-rule{left:0;top:0;width:946px;height:3px;background:var(--blue)}
.brand{left:158px;top:0;width:86px;height:53px;background:#fff;display:flex;align-items:center;justify-content:center;gap:4px;font-family:"Lato",sans-serif;font-weight:700;font-size:13px;color:var(--blue)}
.brand-dot{width:9px;height:9px;border-radius:50%;background:var(--blue)}
.nav{left:462px;top:3px;display:flex;height:32px;align-items:center;font-family:"Lato",sans-serif;font-weight:700;font-size:9.5px;color:#fff;letter-spacing:.2px}
.nav a{color:#fff;text-decoration:none;padding:0 8px;border-left:1px solid #777;line-height:10px}
.nav a.current{background:var(--blue);border:none;height:32px;line-height:32px;padding:0 13px}
.nav a.current + a{border-left:none}
.hero{left:158px;top:53px;width:630px;height:315px;background:linear-gradient(160deg,#b9a58a,#8e7a66 35%,#c9b9a0 55%,#6f6a6a 100%)}
.hero svg{position:absolute;left:0;top:0}
.hero-line1{left:9px;top:245px;font-family:"Roboto Condensed",sans-serif;font-size:18px;color:var(--blue);letter-spacing:-.3px}
.hero-line1 small{font-size:14px}
.hero-help{left:9px;top:264px;font-family:"Roboto Condensed",sans-serif;font-weight:700;font-size:42px;line-height:42px;color:var(--red);letter-spacing:-1px}
.hero-us{left:107px;top:268px;font-family:"Roboto Condensed",sans-serif;font-size:17px;line-height:17px;color:var(--blue)}
.hero-cn{left:107px;top:285px;font-family:"Roboto Condensed",sans-serif;font-size:17px;line-height:17px;color:#555}
.dots{left:582px;top:295px;display:flex;gap:3px}
.dots span{width:10px;height:10px;background:#fff}
.dots span.on{background:var(--blue)}
.page-bg{left:0;top:368px;width:946px;height:624px;background:linear-gradient(180deg,#fbfbfc,#eceef1)}
.section-title{font-family:"Roboto Condensed",sans-serif;font-size:24px;color:var(--blue);letter-spacing:-.3px}
.mission-title{left:158px;top:384px}
.mission-rule{left:158px;top:418px;width:630px;height:1px;background:#c9c9c9}
.mission-rule-accent{left:158px;top:417px;width:140px;height:3px;background:var(--blue)}
.social-top{left:741px;top:391px;display:flex;gap:6px}
.social-top span{width:12px;height:12px;border-radius:50%;background:#444}
.mission-en{left:158px;top:431px;width:630px;font-size:9.2px;line-height:11px;color:#555;text-align:justify}
.mission-cn{left:158px;top:482px;width:630px;font-family:"Noto Serif SC",serif;font-size:9.6px;line-height:13px;color:var(--cn-blue)}
.divider{left:158px;top:522px;width:630px;height:1px;background:#ddd}
.gallery-title{left:0;width:946px;top:539px;text-align:center;color:var(--red)}
.gallery-title span{background:transparent;padding:0 10px}
.dash-l{left:158px;top:553px;width:222px;border-top:1px dotted #bbb}
.dash-r{left:564px;top:553px;width:224px;border-top:1px dotted #bbb}
.gallery{left:158px;top:580px;width:630px;height:118px;border-radius:8px;background:linear-gradient(180deg,#3a86c6,#2369a9)}
.gallery-shadow{left:170px;top:698px;width:606px;height:10px;background:radial-gradient(ellipse at top,rgba(0,0,0,.25),rgba(0,0,0,0) 70%)}
.arrow{top:621px;width:22px;height:32px;background:var(--blue-deep);border-radius:16px}
.arrow svg{position:absolute;top:11px}
.arrow-l{left:142px}
.arrow-r{left:782px}
.photo{border:2px solid #5f9dd2}
.p1{background:linear-gradient(150deg,#d9cfc0,#b6473f 55%,#efe8df)}
.p2{background:linear-gradient(180deg,#8fbde8,#c7d9ea 45%,#4c6e86 70%,#3f8ec0)}
.p3{background:linear-gradient(170deg,#cbb79c,#7a6a5b 50%,#5b5f6c)}
.p4{background:linear-gradient(160deg,#b99876,#ddd4c6 50%,#c6793e)}
.videos-title{left:158px;top:720px}
.video{left:158px;top:756px;width:363px;height:211px;background:linear-gradient(160deg,#7a6b5c,#3f3833 60%,#5a4e44)}
.video-bar{left:0;bottom:0;width:363px;height:33px;background:linear-gradient(180deg,#2a2a2a,#151515)}
.video-progress{left:0;top:178px;width:363px;height:3px;background:#666}
.video-progress i{display:block;width:203px;height:3px;background:#d01f1f}
.video-time{left:101px;top:188px;font-family:"Lato",sans-serif;font-weight:700;font-size:11px;color:#fff}
.video-time span{color:#aaa;font-weight:400}
.more-title{left:529px;top:752px;font-family:"Roboto Condensed",sans-serif;font-size:17px;color:var(--red)}
.thumb{width:120px;height:84px}
.t1{background:linear-gradient(160deg,#9fb0c2,#c23a2c 55%,#2f4a8c)}
.t2{background:linear-gradient(170deg,#9aaec2,#d8d0c4 55%,#e46a2c)}
.t3{background:linear-gradient(180deg,#e9edf0,#b9b0a4 55%,#b23a2c)}
.t4{background:linear-gradient(160deg,#d9d8c9,#e0c24a 60%,#6b5f58)}
.footer{left:0;top:992px;width:946px;height:208px;background:var(--footer-blue);color:#fff}
.f-head{font-family:"Lato",sans-serif;font-weight:700;font-size:15px}
.f-text{font-size:8.6px;line-height:15px}
.f-small{font-size:7.4px}
.f-rule{height:1px;background:rgba(255,255,255,.25)}
.f-vrule{top:1028px;width:1px;height:156px;background:rgba(255,255,255,.25)}
.f-links{font-size:8px;line-height:13.4px;text-transform:uppercase;letter-spacing:.3px}
.f-follow{font-weight:700;font-size:9.5px}
.f-social span{display:inline-block;width:18px;height:18px;border-radius:50%;background:rgba(255,255,255,.6);margin-right:3px}
.f-brand{left:662px;top:1052px;display:flex;align-items:center;gap:6px;font-family:"Lato",sans-serif;font-weight:700;font-size:24px;color:rgba(255,255,255,.45)}
.f-brand i{width:14px;height:14px;border-radius:50%;background:rgba(255,255,255,.45)}
.f-legal{left:662px;top:1114px;width:130px;font-size:7.6px;line-height:10px}
</style>
</head>
<body>

<header>
  <div class="abs masthead" role="img" aria-label="Collage of paired student photos in dark tones"></div>
  <div class="abs masthead-collage"></div>
  <div class="abs top-rule"></div>
  <div class="abs brand"><span class="brand-dot"></span>Brightfern</div>
  <nav class="abs nav">
    <a class="current" href="#">HOME</a>
    <a href="#">ABOUT US</a>
    <a href="#">EVENTS</a>
    <a href="#">PROGRAMS</a>
    <a href="#">FAQ</a>
    <a href="#">CONTACT</a>
  </nav>

  <section class="abs hero" role="img" aria-label="Group photo of American and Chinese students with teachers in a school hall">
    <svg width="630" height="315" viewBox="0 0 630 315" aria-hidden="true">
      <polygon points="0,237 226,237 310,315 0,315" fill="#ffffff" fill-opacity=".86"/>
    </svg>
    <div class="abs hero-line1">Brightfern World Learning <small>is to</small></div>
    <div class="abs hero-help">HELP</div>
    <div class="abs hero-us">American Students</div>
    <div class="abs hero-cn">Chinese Students</div>
    <div class="abs dots"><span class="on"></span><span></span><span></span></div>
  </section>
</header>

<main>
  <div class="abs page-bg" role="img" aria-label="Faint collage of student photos"></div>

  <h2 class="abs section-title mission-title">OUR MISSION</h2>
  <div class="abs social-top" aria-label="Social links"><span></span><span></span><span></span></div>
  <div class="abs mission-rule"></div>
  <div class="abs mission-rule-accent"></div>
  <p class="abs mission-en">Brightfern World Learning is to help American students and Chinese students to break the barriers between the two different cultures, experiences and education backgrounds by providing a global summer program in the U.S. with American students and Chinese students one to one paired, home stay in US families, intensive learning and culture adventure activities, and get them fully prepared for their college education and career developments in this interdependent world.</p>
  <p class="abs mission-cn" lang="zh">明蕨环球学习旨在通过一对一配对和入住小伙伴家庭，为中美学生提供深度文化了解与交流的平台，进而打破因文化与教育背景的不同而产生的屏障，为这个相互依存的世界准备未来的领导者。</p>
  <div class="abs divider"></div>

  <div class="abs dash-l"></div>
  <div class="abs dash-r"></div>
  <h2 class="abs section-title gallery-title"><span>PHOTO GALLERY</span></h2>

  <div class="abs gallery-shadow"></div>
  <section class="abs gallery" aria-label="Photo gallery">
    <div class="abs photo p1" style="left:11px;top:11px;width:146px;height:95px" role="img" aria-label="Students doing a craft activity in a classroom"></div>
    <div class="abs photo p2" style="left:165px;top:11px;width:146px;height:95px" role="img" aria-label="Students by the lakefront with a city skyline"></div>
    <div class="abs photo p3" style="left:319px;top:11px;width:146px;height:95px" role="img" aria-label="Group of students and teachers indoors"></div>
    <div class="abs photo p4" style="left:473px;top:11px;width:146px;height:95px" role="img" aria-label="Students working together at a table"></div>
  </section>
  <div class="abs arrow arrow-l"><svg width="22" height="10" viewBox="0 0 22 10"><polygon points="9,5 14,1 14,9" fill="#fff"/></svg></div>
  <div class="abs arrow arrow-r"><svg width="22" height="10" viewBox="0 0 22 10"><polygon points="13,5 8,1 8,9" fill="#fff"/></svg></div>

  <h2 class="abs section-title videos-title">PROGRAM VIDEOS</h2>
  <section class="abs video" role="img" aria-label="Program video still of students wearing sunglasses">
    <svg class="abs" style="left:161px;top:68px" width="42" height="42" viewBox="0 0 42 42" aria-hidden="true">
      <circle cx="21" cy="21" r="20" fill="#000" fill-opacity=".35"/>
      <polygon points="16,12 31,21 16,30" fill="#fff" fill-opacity=".8"/>
    </svg>
    <div class="abs video-progress"><i></i></div>
    <div class="abs video-bar"></div>
    <svg class="abs" style="left:20px;top:188px" width="70" height="16" viewBox="0 0 70 16" aria-hidden="true">
      <rect x="2" y="1" width="4" height="14" fill="#ddd"/><rect x="9" y="1" width="4" height="14" fill="#ddd"/>
      <polygon points="46,5 50,5 55,1 55,15 50,11 46,11" fill="#ddd"/>
    </svg>
    <div class="abs video-time">0:58 <span>/ 3:33</span></div>
    <svg class="abs" style="left:206px;top:188px" width="150" height="16" viewBox="0 0 150 16" aria-hidden="true">
      <circle cx="8" cy="8" r="5" fill="none" stroke="#bbb" stroke-width="2"/>
      <circle cx="40" cy="8" r="6" fill="none" stroke="#ddd" stroke-width="2"/><line x1="40" y1="8" x2="40" y2="4" stroke="#ddd" stroke-width="2"/>
      <rect x="64" y="3" width="18" height="10" fill="none" stroke="#fff" stroke-width="2"/>
      <rect x="94" y="2" width="22" height="12" fill="none" stroke="#ddd" stroke-width="2"/>
      <path d="M126 6V2h4M140 2h4v4M144 10v4h-4M130 14h-4v-4" fill="none" stroke="#ddd" stroke-width="2"/>
    </svg>
  </section>

  <h3 class="abs more-title">MORE VIDEOS</h3>
  <div class="abs thumb t1" style="left:532px;top:781px" role="img" aria-label="Two students holding national flags"></div>
  <div class="abs thumb t2" style="left:665px;top:781px" role="img" aria-label="Students posing on a city rooftop"></div>
  <div class="abs thumb t3" style="left:532px;top:880px" role="img" aria-label="Students in a line during a gym activity"></div>
  <div class="abs thumb t4" style="left:665px;top:880px" role="img" aria-label="Students at a yellow table in a classroom"></div>
</main>

<footer>
  <div class="abs footer"></div>
  <div class="abs f-vrule" style="left:318px"></div>
  <div class="abs f-vrule" style="left:514px"></div>
  <div class="abs f-vrule" style="left:638px"></div>

  <h4 class="abs f-head" style="left:158px;top:1013px;color:#fff">Contact Us:</h4>
  <div class="abs f-text" style="left:158px;top:1035px;color:#fff">Colette@BrightfernWorldLearning.Org<br>Phone: 312-555-BFWL(2395)<br>Fax: 847-555-0142</div>
  <div class="abs f-rule" style="left:158px;top:1089px;width:138px"></div>
  <div class="abs f-text" style="left:158px;top:1101px;color:#fff">China Tel: 9500-012-3344<br>ChatLine: 1036482751<br>TalkPost ID:<br>ColetteMarin<br>ClassNet: Colette Marin</div>
  <div class="abs f-small" style="left:158px;top:1177px;color:#fff">MicroPost: Brightfern World Learning</div>

  <div class="abs f-text" style="left:338px;top:1035px;color:#fff">Alder Hall School Of Commerce<br>Westbrook University 2200 N. Westbrook<br>Boulevard Lakemont, IL 60199</div>
  <div class="abs f-rule" style="left:338px;top:1089px;width:154px"></div>
  <div class="abs f-small" style="left:338px;top:1104px;line-height:12.5px;color:#fff;font-size:8px">Jade River Travel Service Co.,<br>Ltd. Beijing Eastgate Branch</div>
  <div class="abs f-text" style="left:338px;top:1128px;color:#fff">Tel: 010-55501234<br>Fax: 010-55505678<br>Wen Hao: 139 5550 1122<br>Lin Qiu: 135 5550 3344</div>

  <h4 class="abs f-head" style="left:537px;top:1013px;color:#fff">About Us:</h4>
  <div class="abs f-links" style="left:537px;top:1036px;color:#fff">Company Profile<br>Contact Us<br>Facts &amp; Figures<br>Our History</div>
  <div class="abs f-follow" style="left:537px;top:1104px;color:#fff">FOLLOW Us:</div>
  <div class="abs f-social" style="left:537px;top:1122px" aria-label="Social links"><span></span><span></span><span></span></div>

  <div class="abs f-brand"><i></i>Brightfern</div>
  <div class="abs f-legal" style="color:#fff">Privacy Policy Terms &amp; Conditions<br><span style="display:block;margin-top:3px">Copyright 2013, Brightfern, All Rights Reserved.</span></div>
</footer>

</body>
</html>
```